Need a Facebook image for childcare advertisement

We are after a design for Facebook advertisement for childcare and kindergarten centre enrolments for 2023.

I have attached a previous flyer that we have in pdf format. The new logo is also attached with this brief.

All other information is still current as per the attached flyer.

You can use same colours as per attached flyer. I will also attached some stock images that you can select to use for the design.

our website for your reference:

https://tallowmere-vale.com.au

```html
<!DOCTYPE html>
<html lang="en">
<head>
<meta charset="utf-8">
<title>Tallowmere Vale – Enrolments 2023</title>
<link href="https://fonts.googleapis.com/css2?family=Baloo+2:wght@600;700;800&display=swap" rel="stylesheet">
<style>
  :root {
    --sky: #58aee2;
    --navy: #0d3f80;
    --red: #ee4040;
    --white: #ffffff;
    --cloud: #eef4f8;
    --ring-yellow: #f9d43a;
    --ring-orange: #f7a21d;
    --ring-red: #ef5a2a;
    --photo-warm: #d9c3ae;
    --photo-cool: #8fa9c4;
  }
  * { margin: 0; padding: 0; box-sizing: border-box; }
  html, body { width: 1200px; height: 1200px; overflow: hidden; }
  body { font-family: "Baloo 2", "Arial Rounded MT Bold", sans-serif; }
  .ad {
    position: relative;
    width: 1200px;
    height: 1200px;
    background: var(--sky);
    overflow: hidden;
  }
  .ad__art { position: absolute; inset: 0; }
  .brand {
    position: absolute;
    left: 70px;
    top: 70px;
    width: 370px;
    text-align: center;
    color: var(--navy);
    font-weight: 800;
    line-height: 1;
  }
  .brand__name { font-size: 50px; letter-spacing: 1px; }
  .brand__sub { font-size: 50px; font-size: 21px; margin-top: 10px; letter-spacing: 0.5px; }
  .headline {
    position: absolute;
    left: 61px;
    top: 515px;
    color: var(--navy);
    font-weight: 800;
    font-size: 74px;
    line-height: 76px;
  }
  .headline__accent {
    display: block;
    color: var(--red);
    font-size: 60px;
    line-height: 66px;
  }
  .headline__year {
    display: block;
    color: var(--red);
    font-size: 132px;
    line-height: 118px;
    margin-top: 2px;
  }
  .cta {
    position: absolute;
    left: 61px;
    top: 958px;
    color: var(--navy);
    font-weight: 700;
    font-size: 35px;
    line-height: 43px;
  }
  .site-link {
    position: absolute;
    left: 61px;
    top: 1074px;
    width: 484px;
    height: 59px;
    border-radius: 12px;
    background: var(--navy);
    color: var(--white);
    font-weight: 700;
    font-size: 24px;
    display: flex;
    align-items: center;
    padding-left: 20px;
    text-decoration: none;
  }
</style>
</head>
<body>
<main class="ad">
  <svg class="ad__art" width="1200" height="1200" viewBox="0 0 1200 1200" aria-hidden="false">
    <defs>
      <clipPath id="photo-clip">
        <circle cx="935" cy="360" r="470"/>
        <rect x="935" y="0" width="265" height="360"/>
        <rect x="700" y="0" width="500" height="300"/>
      </clipPath>
      <linearGradient id="ring-grad" x1="0" y1="0" x2="1" y2="1">
        <stop offset="0" stop-color="var(--ring-yellow)"/>
        <stop offset="0.55" stop-color="var(--ring-orange)"/>
        <stop offset="1" stop-color="var(--ring-red)"/>
      </linearGradient>
      <linearGradient id="photo-grad" x1="0" y1="0" x2="1" y2="1">
        <stop offset="0" stop-color="var(--photo-warm)"/>
        <stop offset="0.6" stop-color="var(--photo-cool)"/>
        <stop offset="1" stop-color="#e9e4de"/>
      </linearGradient>
    </defs>

    <circle class="rainbow-ring" cx="935" cy="360" r="500" fill="none" stroke="url(#ring-grad)" stroke-width="60" opacity="0.85"/>

    <g clip-path="url(#photo-clip)">
      <rect class="hero-photo" x="400" y="0" width="800" height="860" fill="url(#photo-grad)"
            role="img" aria-label="Photo of a toddler in a denim dress playing with colourful building blocks"/>
    </g>

    <g class="cloud cloud--logo" fill="var(--white)">
      <path d="M0 0 H640 C650 60 610 110 560 120 C570 190 520 250 450 245 C420 280 350 285 310 255 C270 280 200 280 170 250 C120 270 60 255 40 220 C20 230 8 232 0 230 Z"/>
    </g>

    <g class="cloud cloud--small" fill="var(--cloud)">
      <path d="M508 112 a16 16 0 0 1 22-14 a22 22 0 0 1 40 2 a14 14 0 0 1 22 12 Z"/>
      <path d="M512 568 a20 20 0 0 1 28-18 a28 28 0 0 1 52 4 a18 18 0 0 1 72 14 Z"/>
      <path d="M882 908 a20 20 0 0 1 28-18 a28 28 0 0 1 52 4 a18 18 0 0 1 74 14 Z"/>
    </g>

    <g class="cloud cloud--footer" fill="var(--white)">
      <path d="M590 1200 C600 1150 650 1130 700 1145 C720 1100 780 1085 820 1110 C850 1070 900 1060 940 1085 C970 1030 1040 1010 1100 1040 C1140 1020 1180 1025 1200 1035 V1200 Z"/>
    </g>
  </svg>

  <div class="brand">
    <div class="brand__name">TALLOWMERE VALE</div>
    <div class="brand__sub">EARLY CHILDHOOD LEARNING CENTRE</div>
  </div>

  <h1 class="headline">
    Childcare &amp;<br>kindergarten<br>Centre
    <span class="headline__accent">enrolments for</span>
    <span class="headline__year">2023</span>
  </h1>

  <p class="cta">Contact us to secure<br>your child's spot</p>

  <a class="site-link" href="https://tallowmere-vale.com.au/">https://www.tallowmere-vale.com.au/</a>
</main>
</body>
</html>
```